Health supplement brand needs a new logo for flagship product launch

I have attached a Word document to the brief which gives more detail.

There are 3 different products that we will sell. The label should be interchangeable across all 3 products, where only the colours change. This requires both a selection of a font typface to match our style and a new image embedded in the logo.

Target Market(s)

The target customer is women aged between 25 and 60. We would like to cross over between both audiences, without ruling one out

Font styles to use
Sans Serif

Requirements
Must have
• - It must be eye catching, i.e. people need to stop scrolling when they see it.
- It must have contemporary colours that are popular with women, i.e. pinks, apricots, dark greens, mustards, etc
- The image needs to be very feminine, just like the target audience
- The label must evoke some emotion, yet still be a little bit fun without being too serious.
- The label must use this image below as the main foundation. I have included the EPS file with this email.
Nice to have
• - We want to be somewhere in the middle, as in, the right price point accessible for most people, but still with a bit of class, fun and femininity
Should not have
• - We also don’t want it to look like “just another” nutritional brand selling Tarrow Fieldmix

```html
<!DOCTYPE html>
<html lang="en">
<head>
<meta charset="utf-8">
<title>Lumora Supplement Labels</title>
<link rel="stylesheet" href="https://fonts.googleapis.com/css2?family=Montserrat:wght@400;500&family=Great+Vibes&display=swap">
<style>
  :root {
    --bg: #ffffff;
    --label-base: #fbf3f5;
    --wash-pink: #f3d3df;
    --wash-blush: #f8e4ea;
    --wash-peach: #f6e2d6;
    --brand-ink: #3a3a3a;
    --brand-mint: #8fcab5;
    --tag-green: #6db69c;
    --apricot: #e39464;
    --apricot-soft: #f1b894;
    --rose: #c9748a;
    --rose-soft: #ecaab8;
    --lilac: #a775be;
    --lilac-soft: #c8a2d8;
    --skin: #e9c3b0;
  }
  * { box-sizing: border-box; margin: 0; padding: 0; }
  html, body { width: 1200px; height: 930px; overflow: hidden; background: var(--bg); }
  body { font-family: "Montserrat", sans-serif; position: relative; }

  .label-row {
    position: absolute; top: 90px; left: 0; width: 1200px;
    display: flex; justify-content: center; gap: 38px;
  }
  .label {
    --accent: var(--rose); --accent-soft: var(--rose-soft);
    width: 340px; height: 660px; position: relative; overflow: hidden;
    background: var(--label-base);
    border-radius: 6px;
    box-shadow: 0 6px 24px rgba(120, 90, 100, 0.12);
  }
  .label--thrive { --accent: var(--apricot); --accent-soft: var(--apricot-soft); }
  .label--glow   { --accent: var(--rose);    --accent-soft: var(--rose-soft); }
  .label--renew  { --accent: var(--lilac);   --accent-soft: var(--lilac-soft); }

  .label__wash {
    position: absolute; inset: 92px 0 0 0;
    background:
      radial-gradient(circle at 20% 30%, var(--wash-pink) 0, transparent 45%),
      radial-gradient(circle at 80% 60%, var(--wash-blush) 0, transparent 50%),
      radial-gradient(circle at 30% 85%, var(--wash-pink) 0, transparent 40%),
      radial-gradient(circle at 70% 15%, var(--wash-peach) 0, transparent 40%),
      var(--wash-blush);
  }
  .label__head {
    position: absolute; top: 0; left: 0; right: 0; height: 92px;
    background: #fff; display: flex; align-items: center; justify-content: center;
  }
  .brand { display: flex; align-items: center; gap: 8px; }
  .brand__dot { width: 10px; height: 10px; border-radius: 50%; background: var(--brand-mint); }
  .brand__name { font-weight: 400; font-size: 22px; letter-spacing: 5px; color: var(--brand-ink); }

  .label__body { position: absolute; top: 92px; left: 0; right: 0; bottom: 0; }
  .product-title {
    margin-top: 42px; text-align: center; color: var(--accent);
    font-weight: 500; font-size: 36px; line-height: 1.25; letter-spacing: 0.5px;
  }
  .product-title--single { margin-top: 70px; }

  .stroke-band { position: relative; margin: 20px auto 0; width: 300px; height: 110px; }
  .stroke-band__paint {
    position: absolute; inset: 10px 0;
    background: linear-gradient(90deg, transparent 0, var(--accent-soft) 8%, var(--accent) 50%, var(--accent-soft) 92%, transparent 100%);
    opacity: 0.8; border-radius: 40px 10px 40px 12px;
  }
  .stroke-band__script {
    position: absolute; inset: 0; display: flex; align-items: center; justify-content: center;
    font-family: "Great Vibes", cursive; font-size: 62px; color: #fff; white-space: nowrap;
  }
  .product-desc {
    text-align: center; margin-top: 8px;
    font-size: 14px; color: var(--tag-green); transform: rotate(-2deg);
  }

  .figure {
    position: absolute; right: 22px; bottom: 80px; width: 140px; height: 230px;
    border-radius: 70px 70px 30px 30px;
    background: linear-gradient(180deg, transparent 0, var(--skin) 60%, var(--accent-soft) 100%);
    opacity: 0.55;
  }
  .benefits {
    position: absolute; left: 18px; right: 40px; bottom: 22px;
    padding-bottom: 6px; border-bottom: 1px solid var(--accent);
    font-size: 12px; font-weight: 500; letter-spacing: 0.5px; color: var(--accent);
    white-space: nowrap;
  }

  .footer-brand {
    position: absolute; left: 40px; bottom: 40px;
    display: flex; align-items: center; gap: 12px;
  }
  .footer-brand .brand__name { font-size: 40px; letter-spacing: 9px; }
  .footer-brand .brand__dot { width: 16px; height: 16px; }
</style>
</head>
<body>
  <main class="label-row">
    <article class="label label--thrive">
      <div class="label__wash" role="img" aria-label="Soft pink and peach watercolour wash"></div>
      <header class="label__head"><div class="brand"><span class="brand__name">LUMORA</span><span class="brand__dot"></span></div></header>
      <div class="label__body">
        <h2 class="product-title">PreBiotic<br>COLLAGEN</h2>
        <div class="stroke-band">
          <div class="stroke-band__paint" role="img" aria-label="Apricot brush stroke"></div>
          <div class="stroke-band__script">Thrive</div>
        </div>
        <p class="product-desc">Unflavoured 100% Bovine Collagen Powder</p>
        <div class="figure" role="img" aria-label="Line illustration of a seated woman seen from behind"></div>
        <p class="benefits">HAIR | SKIN | NAILS | JOINTS | MUSCLES</p>
      </div>
    </article>

    <article class="label label--glow">
      <div class="label__wash" role="img" aria-label="Soft pink watercolour wash"></div>
      <header class="label__head"><div class="brand"><span class="brand__name">LUMORA</span><span class="brand__dot"></span></div></header>
      <div class="label__body">
        <h2 class="product-title product-title--single">COLLAGEN</h2>
        <div class="stroke-band">
          <div class="stroke-band__paint" role="img" aria-label="Rose pink brush stroke"></div>
          <div class="stroke-band__script">Soft Glow</div>
        </div>
        <p class="product-desc">Unflavoured 100% Bovine Collagen Powder</p>
        <div class="figure" role="img" aria-label="Line illustration of a seated woman seen from behind"></div>
        <p class="benefits">HAIR | SKIN | NAILS | JOINTS | MUSCLES</p>
      </div>
    </article>

    <article class="label label--renew">
      <div class="label__wash" role="img" aria-label="Soft pink and lilac watercolour wash"></div>
      <header class="label__head"><div class="brand"><span class="brand__name">LUMORA</span><span class="brand__dot"></span></div></header>
      <div class="label__body">
        <h2 class="product-title">PreBiotic<br>FIBER</h2>
        <div class="stroke-band">
          <div class="stroke-band__paint" role="img" aria-label="Lilac brush stroke"></div>
          <div class="stroke-band__script">Renew</div>
        </div>
        <p class="product-desc">Unflavoured 100% Bovine Collagen Powder</p>
        <div class="figure" role="img" aria-label="Line illustration of a seated woman seen from behind"></div>
        <p class="benefits">HAIR | SKIN | NAILS | JOINTS | MUSCLES</p>
      </div>
    </article>
  </main>

  <footer class="footer-brand brand">
    <span class="brand__name">LUMORA</span><span class="brand__dot"></span>
  </footer>
</body>
</html>
```